BRAND BOOK design

We are a new swimwear brand. We have a vague idea of what we want. We have some colors we would like to use. We would love someone who can provide simple, sophisticated yet an edgy design for our first brand book. The brand book will contain our campaign photos and you will have to come up with layouts and simple designs to insert these photos and short quotes or descriptions. The brand book will contain our brand identity and express the vibes we want our customers to feel get from our brand.

Target Market(s)

US and Australia

Industry/Entity Type

Fashion

Font styles to use
Other font styles liked:
• Futura Medium

Colors
f9d9e8
cfcfcf
ffffff

Requirements
Must have
• simple modern layout with pop elements.
• photos must be placed with enough space.
• also need minimal space for words.
Nice to have
• Simple layouts that aren't common. Designs that can show our identity.
• Please refer to our website (under construction): www.brightkelphouse.com
Should not have
• mere copies of other brand designs

```html
<!DOCTYPE html>
<html lang="en">
<head>
<meta charset="utf-8">
<title>Brightkelp Brand Book — Contents Spread</title>
<link rel="stylesheet" href="https://fonts.googleapis.com/css2?family=Jost:wght@300;400&display=swap">
<style>
  :root {
    --backdrop: #a3a3a3;
    --paper: #ffffff;
    --paper-shade: #f4f4f4;
    --strip: #e2e2e2;
    --ink: #4a4a4a;
    --ink-soft: #8a8a8a;
    --rule: #9c9c9c;
    --accent-bar: #555555;
    --sky: #dfe8f1;
    --sand: #f3efea;
    --blush: #f9d9e8;
  }
  * { box-sizing: border-box; margin: 0; padding: 0; }
  html, body {
    width: 1200px; height: 900px; overflow: hidden;
    background: var(--backdrop);
    font-family: "Jost", "Futura", sans-serif;
    font-weight: 300;
    color: var(--ink);
  }
  .spread {
    position: absolute; left: 40px; top: 250px;
    width: 1120px; height: 400px;
    display: flex;
    box-shadow: 0 14px 30px rgba(0,0,0,0.25);
  }
  .page { position: relative; width: 560px; height: 400px; background: var(--paper); overflow: hidden; }

  /* left page */
  .contents-strip {
    position: absolute; left: 0; top: 0; width: 210px; height: 100%;
    background: var(--strip);
  }
  .contents-title {
    position: absolute; left: 36px; top: 58px;
    font-size: 17px; letter-spacing: 1px; text-transform: uppercase;
  }
  .title-bar { position: absolute; left: 36px; top: 82px; width: 30px; height: 4px; background: var(--accent-bar); }
  .wordmark {
    position: absolute; left: 36px; bottom: 62px;
    font-size: 22px; letter-spacing: 3px; text-transform: uppercase; color: var(--ink);
  }
  .contents-panel {
    position: absolute; left: 210px; top: 0; width: 350px; height: 100%;
    background: linear-gradient(90deg, var(--paper) 0%, var(--paper) 80%, var(--paper-shade) 100%);
  }
  .toc-entry { position: absolute; left: 24px; width: 280px; font-size: 10px; line-height: 1.25; }
  .toc-entry.align-right { text-align: right; }
  .toc-entry .season { font-size: 11px; text-transform: uppercase; letter-spacing: .5px; }
  .toc-entry .story { font-size: 9px; text-transform: uppercase; letter-spacing: .5px; }
  .toc-entry .credit { font-size: 9px; color: var(--ink-soft); }
  .toc-entry .heading { font-size: 12px; color: var(--ink-soft); }
  .toc-rule { position: absolute; left: 24px; width: 280px; height: 1px; background: var(--rule); }

  /* right page */
  .gutter {
    position: absolute; left: 0; top: 0; width: 40px; height: 100%; z-index: 3;
    background: linear-gradient(90deg, rgba(0,0,0,0.12), rgba(0,0,0,0));
  }
  .campaign-photo {
    position: absolute; left: 0; top: 0; width: 300px; height: 100%;
    background: linear-gradient(180deg, var(--sky) 0%, #eef2f6 45%, var(--sand) 70%, #ece6df 100%);
  }
  .page-bar { position: absolute; left: 470px; top: 40px; width: 28px; height: 4px; background: var(--accent-bar); }
  .brand-copy {
    position: absolute; left: 330px; top: 62px; width: 190px;
    font-size: 7px; line-height: 1.45; color: var(--ink-soft);
  }
  .brand-copy p { margin-bottom: 8px; }
  .brand-copy .divider { width: 10px; height: 1px; background: var(--rule); margin: 0 0 8px; }
  .brand-copy .tagline { text-transform: uppercase; letter-spacing: .3px; }
  .ghost-wordmark {
    position: absolute; left: 40px; bottom: 12px; z-index: 2;
    font-size: 62px; letter-spacing: 6px; text-transform: uppercase;
    color: rgba(90,90,90,0.09); white-space: nowrap;
  }
  .folio {
    position: absolute; right: 40px; bottom: 26px;
    display: flex; align-items: center; gap: 8px;
    font-size: 8px; color: var(--ink-soft);
  }
  .folio .sep { width: 1px; height: 12px; background: var(--rule); }
  .folio .num {
    width: 14px; height: 14px; border: 1px solid var(--rule); border-radius: 50%;
    display: flex; align-items: center; justify-content: center; font-size: 7px;
  }
</style>
</head>
<body>
  <main class="spread">
    <section class="page page-contents">
      <div class="contents-strip"></div>
      <h1 class="contents-title">Contents</h1>
      <div class="title-bar"></div>
      <div class="wordmark">Brightkelp</div>

      <div class="contents-panel">
        <div class="toc-entry align-right" style="top:64px"><span class="heading">About Us</span></div>
        <div class="toc-rule" style="top:86px"></div>

        <div class="toc-entry" style="top:104px">
          <div class="season">Spring 2018</div>
          <div class="story">The Girl Next Door</div>
          <div class="credit">with Marla Quint</div>
        </div>
        <div class="toc-rule" style="top:152px"></div>

        <div class="toc-entry align-right" style="top:168px">
          <div class="season">Spring 2017</div>
          <div class="story">The Girl Next Door</div>
          <div class="credit">with Marla Quint</div>
        </div>
        <div class="toc-rule" style="top:216px"></div>

        <div class="toc-entry" style="top:262px">
          <div class="heading">Shipping &amp;<br>Exchanges</div>
        </div>
        <div class="toc-rule" style="top:300px"></div>
      </div>
    </section>

    <section class="page page-about">
      <div class="campaign-photo" role="img" aria-label="Campaign photograph: model in a white sun hat and white bikini on a sunny beach"></div>
      <div class="gutter"></div>
      <div class="page-bar"></div>

      <div class="brand-copy">
        <p>A BRIGHTKELP girl is naturally beautiful and confident in her own skin. She is unpretentious, relaxed and at ease. Her style is simple and fun. She loves the ocean and long summer days.</p>
        <p>She is full of life and laughter. She loves the water, and the warmth of the sun on her shoulders.</p>
        <div class="divider"></div>
        <p>Our pieces are cut from soft, durable fabrics and finished with care to last many seasons.</p>
        <p>Every design is made to flatter and to move with you, from the first swim to the last sunset.</p>
        <p>Our swimwear and resort wear pieces are tailored to perfection.</p>
        <p class="tagline">Brightkelp from sunrise to sunset, just another day for you.</p>
      </div>

      <div class="ghost-wordmark" aria-hidden="true">Brightkelp</div>

      <footer class="folio">
        <span>Quint Management</span>
        <span class="sep"></span>
        <span class="num">5</span>
      </footer>
    </section>
  </main>
</body>
</html>
```